Sales and Lettings Boards

Hello, please see attached our sales and lettings boards for our estate agency. These were "designed" by the sign writers. As you can see they are pretty flat and boring - could you work your magic and make them stand out please? I've also attached the logo files. Many thanks, Glen

Target Market(s)

Consumers - residential sale property sales and lettings

Industry/Entity Type

Real Estate Agent

```html
<!DOCTYPE html>
<html lang="en">
<head>
<meta charset="utf-8">
<title>Halden Property – For Sale Board</title>
<link rel="stylesheet" href="https://fonts.googleapis.com/css2?family=Montserrat:wght@500;700&family=Roboto:ital,wght@0,700;1,900&family=Roboto+Condensed:wght@700&display=swap">
<style>
  :root {
    --brand-green: #62b847;
    --charcoal: #4b4c4e;
    --white: #ffffff;
    --band-grey: #c9cac9;
    --band-light: #f4f4f4;
  }
  html, body {
    margin: 0;
    padding: 0;
    width: 1200px;
    height: 900px;
    overflow: hidden;
    background: var(--white);
  }
  .board {
    position: relative;
    width: 1200px;
    height: 900px;
    background: var(--white);
    overflow: hidden;
  }
  .side-stripe {
    position: absolute;
    left: 0; top: 0;
    width: 74px; height: 900px;
    background: var(--brand-green);
  }
  .brand-name {
    position: absolute;
    left: 74px; right: 0;
    top: 42px;
    margin: 0;
    text-align: center;
    font-family: "Montserrat", sans-serif;
    font-weight: 700;
    font-size: 232px;
    line-height: 1;
    letter-spacing: 2px;
    color: var(--charcoal);
  }
  .brand-band {
    position: absolute;
    left: 74px; top: 298px;
    width: 1000px; height: 80px;
    background: linear-gradient(90deg, var(--band-grey) 0%, var(--band-light) 45%, var(--band-light) 60%, var(--band-grey) 85%, rgba(255,255,255,0) 100%);
  }
  .brand-tagline {
    position: absolute;
    left: 404px; top: 290px;
    margin: 0;
    font-family: "Montserrat", sans-serif;
    font-weight: 500;
    font-size: 94px;
    line-height: 1;
    letter-spacing: -2px;
    color: var(--brand-green);
  }
  .key-illustration {
    position: absolute;
    left: 724px; top: 288px;
    width: 452px; height: 436px;
    background: radial-gradient(ellipse at 55% 55%, #e6e7e8 0%, #d2d3d4 40%, rgba(255,255,255,0) 72%);
  }
  .status {
    position: absolute;
    left: 112px; top: 470px;
    margin: 0;
    font-family: "Roboto", sans-serif;
    font-weight: 700;
    font-size: 150px;
    line-height: 1;
    color: var(--brand-green);
  }
  .divider {
    position: absolute;
    left: 117px; top: 624px;
    width: 611px; height: 3px;
    background: var(--charcoal);
  }
  .phone {
    position: absolute;
    left: 112px; top: 636px;
    margin: 0;
    font-family: "Roboto Condensed", sans-serif;
    font-weight: 700;
    font-size: 116px;
    line-height: 1;
    letter-spacing: 1px;
    color: var(--charcoal);
  }
  .footer-band {
    position: absolute;
    left: 74px; top: 762px;
    width: 1126px; height: 138px;
    background: var(--charcoal);
  }
  .web-address {
    position: absolute;
    left: 117px; top: 785px;
    margin: 0;
    font-family: "Roboto", sans-serif;
    font-style: italic;
    font-weight: 900;
    font-size: 58px;
    line-height: 1;
    letter-spacing: 3px;
    color: var(--white);
  }
</style>
</head>
<body>
  <div class="board">
    <div class="side-stripe"></div>

    <h1 class="brand-name">HALDEN</h1>
    <div class="brand-band"></div>
    <p class="brand-tagline">PROPERTY</p>

    <div class="key-illustration" role="img" aria-label="Silver house-shaped key fob with a key on a ring"></div>

    <p class="status">FOR SALE</p>
    <div class="divider"></div>
    <p class="phone">01632 960415</p>

    <div class="footer-band"></div>
    <p class="web-address">WWW.HALDEN-ESTATES.CO.UK</p>
  </div>
</body>
</html>
```